Hi, Looking for an upgraded business card to the aged one attached. Open to suggestions and no real limitations, but if your going to use a picture of a taxi i think it should be vector based rather than a full color picture. I've uploaded a 2 pictures of the type of taxi which is a Velmora K7 in white. The taxi markings look like the pink one in the picture but to be clear his is white. The taxi is in Bermuda so if you wanted to include something island based that's ok as well but not required. The other thing he wanted to keep on there was the bermuda police crest, with the retired police office incorporated somehow.

Requirements
Must have
• Bermuda Taxi Operator
Retired Police Officer
Police Crest
Taxi #
Email
Mobile Number

```html
<!DOCTYPE html>
<html lang="en">
<head>
<meta charset="utf-8">
<title>Bermuda Taxi Operator – Business Card</title>
<link rel="stylesheet" href="https://fonts.googleapis.com/css2?family=Montserrat:wght@400;600;800&display=swap">
<style>
  :root {
    --brand-blue: #2f6aa5;
    --ink-grey: #4a4a4a;
    --soft-grey: #8a8a8a;
    --sliver-grey: #d9d9d9;
    --card-white: #ffffff;
    --backdrop: #e9eaec;
  }
  * { box-sizing: border-box; margin: 0; padding: 0; }
  html, body { width: 1200px; height: 800px; overflow: hidden; }
  body {
    background: var(--backdrop);
    font-family: "Montserrat", Arial, sans-serif;
    display: flex;
    align-items: center;
    justify-content: center;
    gap: 40px;
  }
  .card {
    position: relative;
    width: 540px;
    height: 309px;
    background: var(--card-white);
    overflow: hidden;
    box-shadow: 0 6px 18px rgba(0,0,0,0.12);
  }
  .card__bands { position: absolute; inset: 0; width: 100%; height: 100%; }

  /* Front */
  .front__title {
    position: absolute;
    left: 26px; top: 60px;
    color: var(--brand-blue);
    font-weight: 800;
    font-size: 29px;
    line-height: 1.05;
    letter-spacing: 0.5px;
    text-transform: uppercase;
  }
  .front__vehicle {
    position: absolute;
    left: 24px; top: 132px;
    width: 260px; height: 150px;
    border-radius: 30px 50px 14px 14px;
    background: linear-gradient(160deg, #f4f4f4 0%, #dcdcdc 60%, #bdbdbd 100%);
  }
  .front__identity {
    position: absolute;
    right: 28px; top: 22px;
    width: 210px;
    text-align: center;
  }
  .brand-mark {
    display: inline-flex;
    align-items: center;
    gap: 6px;
    color: var(--brand-blue);
    font-weight: 600;
    font-size: 11px;
    letter-spacing: 1px;
    text-transform: uppercase;
  }
  .brand-mark__dot {
    width: 14px; height: 14px;
    border-radius: 50%;
    background: var(--brand-blue);
  }
  .front__name {
    margin-top: 22px;
    color: var(--ink-grey);
    font-weight: 800;
    font-size: 17px;
    letter-spacing: 0.5px;
    text-transform: uppercase;
  }
  .front__role {
    color: var(--soft-grey);
    font-size: 11.5px;
    font-weight: 400;
  }
  .front__rule {
    width: 70px; height: 2px;
    margin: 6px auto 0;
    background: var(--brand-blue);
  }
  .contact-list {
    position: absolute;
    right: 26px; top: 152px;
    list-style: none;
  }
  .contact-list__item {
    display: flex;
    justify-content: flex-end;
    align-items: center;
    gap: 10px;
    height: 24px;
    color: var(--ink-grey);
    font-size: 11.5px;
  }
  .contact-list__icon {
    width: 16px; height: 16px;
    border-radius: 3px;
    background: var(--ink-grey);
    display: flex; align-items: center; justify-content: center;
  }
  .contact-list__icon--blue { background: var(--brand-blue); }

  /* Back */
  .back__mark {
    position: absolute;
    inset: 0;
    display: flex;
    flex-direction: column;
    align-items: center;
    justify-content: center;
    gap: 14px;
    color: var(--brand-blue);
    font-weight: 600;
    font-size: 22px;
    letter-spacing: 2px;
    text-transform: uppercase;
  }
  .back__mark-dot {
    width: 70px; height: 70px;
    border-radius: 50%;
    background: var(--brand-blue);
  }
</style>
</head>
<body>

  <section class="card card--front">
    <svg class="card__bands" viewBox="0 0 540 309" aria-hidden="true">
      <polygon points="276,309 302,309 318,270" fill="var(--sliver-grey)"/>
      <polygon points="300,309 322,262 540,240 540,309" fill="var(--brand-blue)"/>
    </svg>

    <h1 class="front__title">Bermuda<br>Taxi Operator</h1>

    <div class="front__vehicle" role="img" aria-label="White Velmora K7 passenger van, side three-quarter view"></div>

    <div class="front__identity">
      <div class="brand-mark"><span class="brand-mark__dot"></span>Harbour Watch</div>
      <p class="front__name">Dorian Castell</p>
      <p class="front__role">Retired Police Officer</p>
      <div class="front__rule"></div>
    </div>

    <ul class="contact-list">
      <li class="contact-list__item">Taxi # T2481
        <span class="contact-list__icon">
          <svg width="12" height="12" viewBox="0 0 12 12"><rect x="1" y="4" width="10" height="5" rx="1" fill="#fff"/><rect x="3" y="2" width="6" height="3" fill="#fff"/><circle cx="3.5" cy="9.5" r="1.2" fill="#4a4a4a"/><circle cx="8.5" cy="9.5" r="1.2" fill="#4a4a4a"/></svg>
        </span>
      </li>
      <li class="contact-list__item">1-441-555-0142
        <span class="contact-list__icon contact-list__icon--blue">
          <svg width="12" height="12" viewBox="0 0 12 12"><path d="M3 1.5 L5 3.5 L4 5 Q5 7 7 8 L8.5 7 L10.5 9 L9 10.5 Q4 10 1.5 3 Z" fill="#fff"/></svg>
        </span>
      </li>
      <li class="contact-list__item">dcastell27@postbay.com
        <span class="contact-list__icon contact-list__icon--blue">
          <svg width="12" height="12" viewBox="0 0 12 12"><rect x="1.5" y="3" width="9" height="6" fill="none" stroke="#fff" stroke-width="1"/><polyline points="1.5,3 6,6.5 10.5,3" fill="none" stroke="#fff" stroke-width="1"/></svg>
        </span>
      </li>
    </ul>
  </section>

  <section class="card card--back">
    <svg class="card__bands" viewBox="0 0 540 309" aria-hidden="true">
      <polygon points="400,0 540,0 540,80 430,30" fill="var(--brand-blue)"/>
      <polygon points="0,250 40,280 70,309 0,309" fill="var(--brand-blue)"/>
    </svg>
    <div class="back__mark">
      <span class="back__mark-dot"></span>
      Harbour Watch
    </div>
  </section>

</body>
</html>
```